Business Card Design

We need a business card design for a Non-Profit Christian Based Organization located in Milford, Pa.
Alder Ridge Open Door Relief
Is a Christ-centered organization dedicated to providing compassion and hope to homeless or near homeless, families and individuals, by meeting their basic and urgent need of food, clothing and shelter.
Updates
the logo is black and white
and must add the color green some where 00400
Industry/Entity Type
Clothing
Contact Information for Business Card
Alder Ridge Open Door Relief
P.O. Box 817
Fernvale, Pa 18402
Phone: (570) 384-CARE(2273)
Toll Free: (855) 384-CARE
email:Info@alderridgeodr.org
email:Careline@alderridgeodr.org
Our organization already has a logo.
Front of card:
Is a Christ-centered organization dedicated to providing compassion and hope to homeless or near homes, families and individual by meeting their basic and urgent need of food, clothing and shelter.(this is our Mission Statement)
On back of card:
'I was hungry and you gave me something to eat;
"I was thirsty and you gave me something to drink;
"I was a stranger and you invited me in."
Matthew 25:35
Color: Logo is black and white
Background color I would like a bright light green 00ff00(close to that)
I attached a sample of what I created on Quill Press but, I don't like the color green, nor the design (but I just wanted to give you and Idea of the Logo and Alder Ridge (one line) Open Door Relief (second line) in a different font thank you
Colette Marsh
Pr/Board of Directors

```html
<!DOCTYPE html>
<html lang="en">
<head>
<meta charset="utf-8">
<title>Alder Ridge Open Door Relief – Business Card</title>
<link rel="stylesheet" href="https://fonts.googleapis.com/css2?family=Gochi+Hand&family=Source+Sans+3:wght@400&display=swap">
<style>
  :root {
    --stage: #e9e7e2;
    --card-white: #ffffff;
    --brand-green: #a8cc3a;
    --back-green: #acd038;
    --ink: #1a1a1a;
    --art-light: #f2f2f2;
    --art-dark: #1e1e1e;
  }
  html, body {
    margin: 0;
    padding: 0;
    overflow: hidden;
  }
  body {
    width: 1200px;
    height: 960px;
    background: var(--stage);
    position: relative;
    font-family: "Source Sans 3", sans-serif;
  }
  .card {
    position: absolute;
    width: 720px;
    height: 410px;
    box-shadow: 0 6px 18px rgba(0,0,0,0.18);
    box-sizing: border-box;
    overflow: hidden;
  }
  /* Front */
  .card-front {
    left: 60px;
    top: 50px;
    background: var(--card-white);
  }
  .front-art {
    position: absolute;
    left: 50px;
    top: 60px;
    width: 105px;
    height: 170px;
    border-radius: 40px 20px 50px 30px;
    background: linear-gradient(135deg, var(--art-light) 0%, #bdbdbd 45%, var(--art-dark) 100%);
  }
  .org-name {
    position: absolute;
    left: 172px;
    top: 38px;
    margin: 0;
    font-family: "Gochi Hand", cursive;
    font-weight: 400;
    font-size: 40px;
    line-height: 48px;
    color: var(--brand-green);
    white-space: nowrap;
  }
  .mission {
    position: absolute;
    left: 176px;
    top: 94px;
    width: 500px;
    margin: 0;
    font-family: "Gochi Hand", cursive;
    font-size: 19px;
    line-height: 30px;
    color: var(--ink);
  }
  .contact {
    position: absolute;
    margin: 0;
    font-size: 20px;
    line-height: 32px;
    color: var(--brand-green);
    white-space: nowrap;
  }
  .contact-postal { left: 62px; bottom: 26px; }
  .contact-online { right: 40px; top: 248px; text-align: right; }
  /* Back */
  .card-back {
    left: 440px;
    top: 500px;
    background: var(--back-green);
  }
  .back-art {
    position: absolute;
    left: 40px;
    top: -10px;
    width: 225px;
    height: 370px;
    border-radius: 0 0 90px 60px;
    background: linear-gradient(120deg, var(--art-light) 0%, #9a9a9a 50%, var(--art-dark) 100%);
  }
  .verse {
    position: absolute;
    left: 292px;
    top: 72px;
    width: 395px;
    margin: 0;
    font-family: "Gochi Hand", cursive;
    font-size: 26px;
    line-height: 40px;
    color: var(--ink);
  }
  .verse-ref {
    display: block;
    padding-left: 125px;
  }
</style>
</head>
<body>

  <section class="card card-front">
    <div class="front-art" role="img" aria-label="Black and white illustration of two clasped hands"></div>
    <h1 class="org-name">Alder Ridge Open Door Relief</h1>
    <p class="mission">Is a Christ-centered organization dedicated to providing compassion and hope to homeless or near homes, families and individual by meeting their basic and urgent need of food, clothing and shelter.</p>
    <p class="contact contact-online">
      Info@alderridgeodr.org<br>
      Careline@alderridgeodr.org<br>
      alderridgeodr.org
    </p>
    <p class="contact contact-postal">
      Alder Ridge Open Door Relief<br>
      P.O. Box 817 Fernvale, Pa 18402<br>
      Phone: (570) 384-CARE(2273)<br>
      Toll Free: (855) 384-CARE
    </p>
  </section>

  <section class="card card-back">
    <div class="back-art" role="img" aria-label="Large illustration of two clasped hands, one white and one black"></div>
    <p class="verse">
      'I was hungry and you gave me something to eat; "I was thirsty and you gave me something to drink; "I was a stranger and you invited me in."
      <span class="verse-ref">~ Matthew 25:35</span>
    </p>
  </section>

</body>
</html>
```